Product labels for new supplements business targeting high performing creative people

I need a label design for different supplements like Whey, BCAA, Melatonin etc. that I could customize for each use case separately.

The brand is called lanternfolk.life, and it would be the first design of the labels. We haven't sold any products yet, but the target audience is people with growth mindset, people who want to be as efficient as possible and are constantly looking to improve their lifestyle. As part of that, they are also working out, but don't know much about supplements yet. Mostly people between 20-34.

I don't have a too specific idea of the expected design, though it should be light, warm, smart and minimalist, maybe have some patterns. It should looks smart and clean (and expensive). Orange and golden might be the additional colors for white. I have attached the templates of some products that I plan to sell and also the logo of the brand.

Here's what I have used for inspiration:
Brands that I like and are somewhat similar in concept: https://www.vimqera.com/ (!!specially the way they
bring "how the product helps them" in focus, not "what the product is" & https://www.pobri.care/ &
https://www.selvoda.com/sport/ & https://en.kambelo.fr/ &
https://gridmarket.com/profiles/corawellhaldesign/designs/417586

Here's how different products look like: https://prodaxel.com/catalog

Target Market(s)

target audience is people with growth mindset, people who want to be as efficient as possible and are constantly looking to improve their lifestyle. As part of that, they are also working out, but don't know much about supplements yet. Mostly people between 20-34.

Industry/Entity Type

Supplements

Font styles to use
Sans Serif

Colors
FFC000
F8CF3A
FAE287
FDF2CF
FEFAEE
F0912C
F2A743
F7CA91
FBE8D2
FDF5EE
EE7325
F08F49
F5BC92
FAE3D3
FDF4ED

Requirements
Must have
• Clean, smart and minimalist design that can be applied for different products in different sizes, like Whey protein, BCAA, vitamins etc. available here: https://prodaxel.com/catalog
Nice to have
• Patterns, expensive look
Should not have
• Doodles, too many colors

```html
<!DOCTYPE html>
<html lang="en">
<head>
<meta charset="utf-8">
<title>lanternfolk.life – Melatonin label</title>
<link rel="stylesheet" href="https://fonts.googleapis.com/css2?family=Bebas+Neue&family=Poppins:wght@300;400;500;600&family=Inter:wght@400;600;800;900&display=swap">
<style>
  :root {
    --canvas: #f4f4f5;
    --white: #ffffff;
    --ink: #111111;
    --orange: #f0912c;
    --orange-deep: #ee7325;
    --red: #e8352a;
    --amber: #f7a23c;
    --cream: #fdf5ee;
  }
  * { box-sizing: border-box; margin: 0; padding: 0; }
  html, body { width: 1200px; height: 1200px; overflow: hidden; }
  body {
    background: var(--canvas);
    font-family: "Poppins", sans-serif;
    color: var(--ink);
    position: relative;
  }
  .label {
    position: absolute;
    left: 60px;
    width: 1080px;
    height: 432px;
    overflow: hidden;
    box-shadow: 0 2px 10px rgba(0,0,0,0.06);
  }
  .label--white { top: 138px; background: var(--white); }
  .label--orange {
    top: 630px;
    background: linear-gradient(160deg, var(--amber) 0%, var(--orange-deep) 55%, var(--red) 100%);
    color: var(--white);
  }

  /* usage column */
  .usage {
    position: absolute;
    left: 20px;
    top: 30px;
    width: 326px;
    text-align: center;
    font-size: 13px;
    line-height: 1.35;
  }
  .usage__tag {
    display: inline-block;
    background: linear-gradient(90deg, var(--orange), var(--orange-deep));
    color: var(--white);
    font-family: "Inter", sans-serif;
    font-weight: 600;
    font-size: 11px;
    padding: 2px 14px;
    border-radius: 12px;
    margin-bottom: 4px;
  }
  .label--orange .usage__tag { background: var(--red); }
  .usage p { margin-bottom: 10px; }
  .usage__warning {
    font-family: "Inter", sans-serif;
    font-weight: 600;
    font-size: 12.5px;
    line-height: 1.35;
  }
  .usage__disclaimer {
    font-size: 10.5px;
    line-height: 1.55;
    margin-top: 14px;
  }

  /* brand + claims column */
  .brand {
    position: absolute;
    left: 363px;
    width: 363px;
    display: flex;
    align-items: center;
    justify-content: center;
    gap: 12px;
    font-family: "Poppins", sans-serif;
    font-weight: 400;
    letter-spacing: 1.5px;
  }
  .label--white .brand { top: 110px; font-size: 28px; color: var(--ink); }
  .label--orange .brand { top: 36px; font-size: 26px; color: var(--white); }
  .brand__dot {
    width: 22px; height: 22px; border-radius: 50%;
    background: var(--orange-deep);
    flex: none;
  }
  .label--orange .brand__dot { background: var(--white); }

  .claims {
    position: absolute;
    left: 363px;
    width: 363px;
    font-family: "Bebas Neue", sans-serif;
    text-align: center;
    line-height: 1;
    color: var(--white);
  }
  .label--white .claims {
    top: 195px;
    height: 104px;
    padding-top: 12px;
    font-size: 42px;
    border-radius: 26px;
    background: linear-gradient(90deg, var(--orange) 0%, var(--orange-deep) 50%, var(--red) 100%);
  }
  .label--orange .claims { top: 190px; font-size: 46px; }
  .claims sup { font-size: 0.6em; }

  .product {
    position: absolute;
    left: 363px;
    width: 363px;
    text-align: center;
  }
  .label--white .product { top: 308px; }
  .label--orange .product { top: 300px; color: var(--ink); }
  .product__name {
    font-weight: 500;
    font-size: 34px;
    letter-spacing: 3px;
    line-height: 1.1;
  }
  .product__dose { font-weight: 600; font-size: 14px; line-height: 1.4; }
  .product__count { font-size: 11.5px; letter-spacing: 1.2px; }

  .category {
    position: absolute;
    text-align: center;
    font-weight: 400;
    font-size: 24px;
    letter-spacing: 2.5px;
    color: var(--white);
  }
  .label--white .category {
    left: 0; right: 0; top: 385px; height: 47px;
    line-height: 47px;
    background: linear-gradient(90deg, var(--orange) 0%, var(--orange-deep) 50%, var(--red) 100%);
  }
  .label--orange .category {
    left: 378px; width: 333px; top: 392px; height: 30px;
    line-height: 30px;
    border-radius: 16px;
    background: rgba(255,255,255,0.22);
  }

  /* supplement facts */
  .facts {
    position: absolute;
    left: 749px;
    top: 22px;
    width: 325px;
    border: 2px solid var(--ink);
    background: var(--white);
    color: var(--ink);
    font-family: "Inter", sans-serif;
    padding: 3px 5px 6px;
  }
  .facts__title { font-weight: 900; font-size: 33px; line-height: 1.05; letter-spacing: -0.3px; }
  .facts__serving { font-size: 10.5px; line-height: 1.2; border-bottom: 6px solid var(--ink); padding-bottom: 3px; }
  .facts table { width: 100%; border-collapse: collapse; font-size: 10.5px; }
  .facts th { font-weight: 800; text-align: right; line-height: 1.05; padding: 3px 0 2px; border-bottom: 3px solid var(--ink); }
  .facts td { padding: 2px 0; border-bottom: 1px solid var(--ink); }
  .facts td.amount { text-align: right; padding-right: 28px; }
  .facts td.dv { text-align: right; width: 20px; }
  .facts tr.last td { border-bottom: 3px solid var(--ink); }
  .facts__note { font-size: 10.5px; padding-top: 4px; }

  .ingredients {
    position: absolute;
    left: 749px;
    top: 218px;
    width: 325px;
    font-family: "Inter", sans-serif;
    font-size: 10.5px;
    line-height: 1.3;
  }
  .maker {
    position: absolute;
    left: 749px;
    top: 324px;
    width: 325px;
    text-align: center;
    font-family: "Inter", sans-serif;
    font-size: 10.5px;
    line-height: 1.45;
  }
</style>
</head>
<body>

<!-- White label -->
<section class="label label--white">
  <div class="usage">
    <span class="usage__tag">SUGGESTED USE:</span>
    <p>As a dietary supplement take 1 (one) tablet 15–30 minutes before bed or as directed by your healthcare professional.</p>
    <span class="usage__tag">CAUTION:</span>
    <p>Do not exceed recommended dose. Pregnant or nursing mothers, children under the age of 18, and individuals with a known medical condition should consult a physician before using this or any dietary supplement.</p>
    <div class="usage__warning">KEEP OUT OF REACH OF CHILDREN. DO NOT USE IF SAFETY SEAL IS DAMAGED OR MISSING. STORE IN A COOL, DRY PLACE.</div>
    <div class="usage__disclaimer">* These statements have not been evaluated by the Food and Drug Administration. This product is not intended to diagnose, treat, cure or prevent any disease.</div>
  </div>

  <div class="brand"><span class="brand__dot"></span>lanternfolk.life</div>
  <div class="claims">FALL ASLEEP FASTER*<br>STAY ASLEEP LONGER*</div>
  <div class="product">
    <div class="product__name">MELATONIN</div>
    <div class="product__dose">1 mg</div>
    <div class="product__count">60 TABLETS</div>
  </div>

  <div class="facts">
    <div class="facts__title">Supplement Facts</div>
    <div class="facts__serving">Serving Size: 1 tablet<br>Servings per container: 60</div>
    <table>
      <tr><th></th><th>Amount per<br>Serving</th><th>% Daily<br>Value</th></tr>
      <tr><td>Calories</td><td class="amount">0.076 Kcal</td><td class="dv">*</td></tr>
      <tr class="last"><td>Melatonin</td><td class="amount">1000 µg</td><td class="dv">*</td></tr>
    </table>
    <div class="facts__note">*Daily Value not established.</div>
  </div>
  <div class="ingredients">Other Ingredients: Microcrystalline cellulose, starch, magnesium salts of fatty acids and silica.</div>
  <div class="maker">Manufactured for and distributed by:<br>[your LLC name here]<br>Address:<br>[your legal address and phone nr or email]</div>

  <div class="category">DIETARY SUPPLEMENT</div>
</section>

<!-- Orange label -->
<section class="label label--orange">
  <div class="usage">
    <span class="usage__tag">SUGGESTED USE:</span>
    <p>As a dietary supplement take 1 (one) tablet 15–30 minutes before bed or as directed by your healthcare professional.</p>
    <span class="usage__tag">CAUTION:</span>
    <p>Do not exceed recommended dose. Pregnant or nursing mothers, children under the age of 18, and individuals with a known medical condition should consult a physician before using this or any dietary supplement.</p>
    <div class="usage__warning">KEEP OUT OF REACH OF CHILDREN. DO NOT USE IF SAFETY SEAL IS DAMAGED OR MISSING. STORE IN A COOL, DRY PLACE.</div>
    <div class="usage__disclaimer">* These statements have not been evaluated by the Food and Drug Administration. This product is not intended to diagnose, treat, cure or prevent any disease.</div>
  </div>

  <div class="brand"><span class="brand__dot"></span>lanternfolk.life</div>
  <div class="claims">FALL ASLEEP FASTER<sup>*</sup><br>STAY ASLEEP LONGER<sup>*</sup></div>
  <div class="product">
    <div class="product__name">MELATONIN</div>
    <div class="product__dose">1 mg</div>
    <div class="product__count">60 TABLETS</div>
  </div>

  <div class="facts">
    <div class="facts__title">Supplement Facts</div>
    <div class="facts__serving">Serving Size: 1 tablet<br>Servings per container: 60</div>
    <table>
      <tr><th></th><th>Amount per<br>Serving</th><th>% Daily<br>Value</th></tr>
      <tr><td>Calories</td><td class="amount">0.076 Kcal</td><td class="dv">*</td></tr>
      <tr class="last"><td>Melatonin</td><td class="amount">1000 µg</td><td class="dv">*</td></tr>
    </table>
    <div class="facts__note">*Daily Value not established.</div>
  </div>
  <div class="ingredients">Other Ingredients: Microcrystalline cellulose, starch, magnesium salts of fatty acids and silica.</div>
  <div class="maker">Manufactured for and distributed by:<br>[your LLC name here]<br>Address:<br>[your legal address and phone nr or email]</div>

  <div class="category">DIETARY SUPPLEMENT</div>
</section>

</body>
</html>
```